Renewable energy company needs modern memorable marketing brochure

We have an 8 page marketing brochure which was created in house. This needs to be revamped and modernised to stand out from our competitors in Australia, Chile and the UK. The brochure should depict us as a professional and dynamic company and instil confidence in prospective clients that we do a professional job. Once the design is finalised we will need a country specific document in the correct language i.e. Spanish for Chile. We are happy to pay for these iterations. We have a company logo which we would like incorporated into the brochure and the colours from the logo utilised where appropriate in the overall design. I have uploaded our existing brochure for an example of the content that the brochure needs to have and can upload the images separately if they are needed. Images in the brochure need to be copyright free and we have lots of photos in-house. I have added all the images from the last brochure and also the text in Indesign so it can be copied easily if needed.

Target Market(s)

landowners and companies

Industry/Entity Type

It Company

Requirements
Must have
• A clean modern look with some colours taken from the logo colour. Be easy to print in various countries.

```html
<!DOCTYPE html>
<html lang="en">
<head>
<meta charset="utf-8">
<title>Brightfield Energy – Solar Farms on Working Farms</title>
<link rel="stylesheet" href="https://fonts.googleapis.com/css2?family=Barlow+Semi+Condensed:wght@400;500&family=Barlow:wght@400&display=swap">
<style>
  :root {
    --teal: #1f9f87;
    --teal-deep: #137a68;
    --teal-pale: #9fd6c8;
    --ink: #6f6f6f;
    --rule: #8a8a8a;
    --rule-light: #a9a9a9;
    --paper: #f7f7f7;
    --paper-right: #f9f9f9;
    --plan-light: #e8ecdd;
    --plan-deep: #c9d8b8;
    --key: #e6e6e6;
  }
  * { box-sizing: border-box; margin: 0; padding: 0; }
  html, body { width: 1200px; height: 908px; overflow: hidden; }
  body {
    background: #dcdcdc;
    font-family: "Barlow", sans-serif;
    color: var(--ink);
  }
  .spread { position: relative; width: 1200px; height: 908px; display: flex; }
  .page { position: relative; width: 600px; height: 908px; }
  .page--left { background: var(--paper); }
  .page--right { background: var(--paper-right); box-shadow: inset 8px 0 14px -10px rgba(0,0,0,.25); }

  .corner-ornament {
    position: absolute; top: 0;
    background: linear-gradient(225deg, var(--teal-pale), var(--teal) 55%, var(--teal-deep));
    opacity: .85;
  }
  .page--left .corner-ornament { left: 10px; width: 112px; height: 138px; }
  .page--right .corner-ornament { left: 0; width: 110px; height: 140px; }

  .page-title {
    position: absolute; left: 135px; top: 78px;
    font-family: "Barlow Semi Condensed", sans-serif; font-weight: 400;
    font-size: 25px; letter-spacing: .2px; color: var(--teal);
  }
  .title-rule { position: absolute; left: 135px; right: 0; top: 111px; border-top: 1px solid var(--rule); }

  .site-plan {
    position: absolute; left: 131px; top: 143px; width: 338px; height: 462px;
    background: linear-gradient(135deg, var(--plan-light), var(--plan-deep));
  }
  .plan-key { position: absolute; left: 140px; top: 614px; width: 110px; height: 64px; background: var(--key); }

  .body-copy { position: absolute; left: 67px; top: 716px; width: 500px; font-size: 10.5px; line-height: 15px; }
  .body-copy p + p { margin-top: 13px; }

  .page-footer {
    position: absolute; left: 61px; right: 40px; top: 881px;
    display: flex; justify-content: space-between;
    font-family: "Barlow Semi Condensed", sans-serif; font-size: 7px; color: var(--teal);
  }
  .page-number { font-weight: 500; }
  .page--right .page-footer { left: 54px; right: 48px; top: 879px; }

  .section-label {
    position: absolute; left: 68px;
    font-family: "Barlow Semi Condensed", sans-serif; font-weight: 400;
    font-size: 16px; color: var(--teal);
  }
  .notes-label { top: 146px; }
  .sketches-label { top: 558px; }
  .notes-lines { position: absolute; left: 68px; top: 188px; width: 466px; }
  .notes-lines span { display: block; height: 20.8px; border-top: 1px solid var(--rule-light); }
  .sketch-box { position: absolute; left: 68px; top: 598px; width: 468px; height: 232px; border: 1px solid var(--rule); }
</style>
</head>
<body>
<main class="spread">
  <section class="page page--left">
    <div class="corner-ornament" role="img" aria-label="Decorative teal geometric corner ornament"></div>
    <h1 class="page-title">SOLAR FARMS ON WORKING FARMS</h1>
    <div class="title-rule"></div>

    <div class="site-plan" role="img" aria-label="Site layout plan of the solar farm showing panel fields A to G with hedgerows"></div>
    <div class="plan-key" role="img" aria-label="Key to the site layout plan"></div>

    <div class="body-copy">
      <p>Brightfield Energy understands that in many cases solar farms need to be incorporated onto a working farm.</p>
      <p>We work closely with landowners to ensure that the layout and operation of the solar farm fits in with the day to day running of the business. The area within and around the panels can be used for sheep grazing and only 5% of the land is actually penetrated by any solar farm structures.</p>
      <p>Caerwen Solar Farm, 5 MWp, 11 Hectares, Wales</p>
    </div>

    <footer class="page-footer"><span>OPENSKY ENERGY Corporate Brochure</span><span class="page-number">01</span></footer>
  </section>

  <section class="page page--right">
    <div class="corner-ornament" role="img" aria-label="Decorative teal geometric corner ornament"></div>

    <h2 class="section-label notes-label">Notes</h2>
    <div class="notes-lines">
      <span></span><span></span><span></span><span></span><span></span><span></span>
      <span></span><span></span><span></span><span></span><span></span><span></span>
      <span></span><span></span><span></span><span></span><span></span>
    </div>

    <h2 class="section-label sketches-label">Sketches</h2>
    <div class="sketch-box"></div>

    <footer class="page-footer"><span>OPENSKY ENERGY Corporate Brochure</span><span class="page-number">01</span></footer>
  </section>
</main>
</body>
</html>
```